Solar Carport

Kestrelvale renewables is looking for a flyer promoting our solar carport design in Alberta, BC and Saskatchewan. We call it the Tinderloft. We have specific color pallet. Should be flashy, endorse local manufacturing, and the over all design should have a green feel to it. We would also like to add this to our website. We will offer this design in steel and wood beam frame.

```html
<!DOCTYPE html>
<html lang="en">
<head>
<meta charset="utf-8">
<title>Kestrelvale Renewables – Tinderloft Solar Carport</title>
<link href="https://fonts.googleapis.com/css2?family=Montserrat:wght@500;600;700;800&display=swap" rel="stylesheet">
<style>
  :root{
    --bg-dark:#1a2c1c;
    --cyan:#5ccde2;
    --lime:#7ac143;
    --frame:#4db848;
    --frame-dark:#2e9a45;
    --band:#48ad4b;
    --band-dark:#1b2c1d;
    --white:#ffffff;
  }
  *{margin:0;padding:0;box-sizing:border-box}
  html,body{width:927px;height:1200px;overflow:hidden;background:var(--bg-dark)}
  .flyer{
    position:relative;width:927px;height:1200px;overflow:hidden;
    font-family:'Montserrat',sans-serif;color:var(--white);
    background:radial-gradient(ellipse 70% 55% at 35% 55%, #11553b 0%, #174430 45%, var(--bg-dark) 100%);
  }
  .locations{
    position:absolute;top:21px;left:353px;display:flex;
    font-weight:700;font-size:18.8px;letter-spacing:.3px;
  }
  .locations span{display:flex;align-items:center;white-space:nowrap}
  .locations span::before{
    content:"";width:12px;height:12px;border-radius:50%;background:var(--lime);margin-right:7px;
  }
  .locations .loc-1{margin-right:18px}
  .locations .loc-2{margin-right:30px}
  .brand{
    position:absolute;top:140px;left:712px;width:160px;
    display:flex;align-items:center;gap:8px;
    font-weight:800;font-size:18px;color:var(--cyan);line-height:1.15;
  }
  .brand .brand-dot{width:14px;height:14px;border-radius:50%;background:var(--cyan);flex:none}
  .timeline{position:absolute;left:0;top:0}
  .heading{
    position:absolute;left:53px;font-weight:800;font-size:43px;line-height:56px;
    color:var(--cyan);letter-spacing:.5px;
  }
  .heading svg{vertical-align:-4px;margin-left:6px}
  .about-title{top:263px}
  .help-title{top:582px}
  .copy{
    position:absolute;left:53px;width:392px;font-size:16.2px;font-weight:500;
    line-height:27.3px;text-align:justify;text-align-last:left;
  }
  .about-copy{top:323px}
  .help-copy{top:701px}
  .closing{position:absolute;left:53px;top:1028px;font-size:16.2px;font-weight:500}
  .photo-frame{
    position:absolute;left:499px;width:385px;height:208px;border-radius:22px;
    background:linear-gradient(135deg,var(--frame) 0%,var(--frame-dark) 60%,var(--frame) 100%);
    box-shadow:0 4px 10px rgba(0,0,0,.35);
  }
  .photo-frame .photo{
    position:absolute;left:11px;top:11px;right:11px;bottom:11px;border-radius:16px;
  }
  .frame-1{top:270px}
  .frame-2{top:487px}
  .frame-3{top:705px}
  .frame-1 .photo{background:linear-gradient(180deg,#6f8c9c 0%,#7c8783 35%,#c77a35 45%,#2a2a2a 70%,#111 100%)}
  .frame-2 .photo{background:linear-gradient(180deg,#777 0%,#6f7376 35%,#3a3f44 55%,#2a2a2a 75%,#111 100%)}
  .frame-3 .photo{background:linear-gradient(180deg,#5f86a8 0%,#7b93a6 45%,#b0753a 58%,#2a2a2a 75%,#111 100%)}
  .contact-band{
    position:absolute;left:0;top:1092px;width:927px;height:108px;background:var(--band);
  }
  .contact-band .line{position:absolute;left:0;width:480px;height:2px;background:var(--band-dark)}
  .contact-band .line-a{top:92px}
  .contact-band .line-b{top:103px}
  .contact-band .corner{position:absolute;left:480px;top:84px;width:447px;height:24px;background:var(--band-dark)}
  .contact{position:absolute;top:40px;font-weight:700;color:var(--white);white-space:nowrap}
  .phone{font-size:27px}
  .phone-1{left:53px}
  .phone-2{left:272px}
  .email{left:496px;top:41px;font-size:21.5px;font-weight:600}
</style>
</head>
<body>
<div class="flyer">
  <div class="locations">
    <span class="loc-1">LARCHMERE VALLEY</span>
    <span class="loc-2">ALBERTA</span>
    <span>CANADA</span>
  </div>

  <div class="brand"><span class="brand-dot"></span><span>KESTRELVALE RENEWABLES</span></div>

  <svg class="timeline" width="927" height="1200" aria-hidden="true">
    <line x1="686" y1="210" x2="686" y2="985" stroke="#7ac143" stroke-width="2" stroke-dasharray="2 4" stroke-linecap="round"/>
    <circle cx="687" cy="197" r="11" fill="#7ac143"/>
    <circle cx="684" cy="996" r="11" fill="#7ac143"/>
  </svg>

  <h1 class="heading about-title">ABOUT US<svg width="34" height="34" viewBox="0 0 34 34"><circle cx="17" cy="17" r="15" fill="none" stroke="#5ccde2" stroke-width="3"/><circle cx="17" cy="17" r="9.5" fill="none" stroke="#5ccde2" stroke-width="3"/><circle cx="17" cy="17" r="4.5" fill="#5ccde2"/></svg></h1>
  <p class="copy about-copy">Kestrelvale Renewables Inc is 100% locally owned and operated by two electrical industry professionals. We saw the shift to less carbon-intensive energy, so we designed the Tinderloft solar carport, manufactured locally in Alberta, to keep our public dollars and jobs from larger international corporations.</p>

  <h2 class="heading help-title">HOW CAN WE<br>HELP?<svg width="34" height="34" viewBox="0 0 34 34"><circle cx="17" cy="17" r="15" fill="none" stroke="#5ccde2" stroke-width="3"/><circle cx="17" cy="17" r="9.5" fill="none" stroke="#5ccde2" stroke-width="3"/><circle cx="17" cy="17" r="4.5" fill="#5ccde2"/></svg></h2>
  <p class="copy help-copy">We strive to be in constant communication with our customers until the solar installation job is done. The Tinderloft carport is offered in a steel or wood beam frame and is installed across Alberta, BC and Saskatchewan. Contact us for your forecasts in solar energy production and customized cost evaluations.<br>Please use the form for your solar carport quote, or call us for any questions about converting your home or business to solar.</p>
  <p class="closing">We look forward to serving you!</p>

  <div class="photo-frame frame-1"><div class="photo" role="img" aria-label="3D render of the wood-beam Tinderloft carport frame seen from the side over a parking lot"></div></div>
  <div class="photo-frame frame-2"><div class="photo" role="img" aria-label="3D render from above of two solar panel arrays on the Tinderloft carport over parking stalls"></div></div>
  <div class="photo-frame frame-3"><div class="photo" role="img" aria-label="3D render of the wood-beam Tinderloft carport viewed from the front under a blue sky"></div></div>

  <footer class="contact-band">
    <span class="contact phone phone-1">403.555.0146</span>
    <span class="contact phone phone-2">780.555.0172</span>
    <span class="contact email">sales@kestrelvalerenewables.com</span>
    <span class="line line-a"></span>
    <span class="line line-b"></span>
    <span class="corner"></span>
  </footer>
</div>
</body>
</html>
```